Steady Ground for Your Venture - book cover

A book cover (front) to be used on print book. Book will be 5 inches by 8 inches. Also need the cover image (as jpg) for promotional purposes. Include company logo on cover - I've included a couple of versions. Include my name as author: Dr. Lorinda Haskell

Title of book is:
Weatherizing Your Enterprise
(sub-title) by teaching thinking skills

this can be a sub-sub title, or a call out or "burst" standing alone -
A survival guide for 21st century business

If you'd like some inspiration, check out my web page: www.lessonmedic.net
The company colors are red, white and blue, but I think red might be too harsh - use with caution if you use it.
RGB values of the company are:
Blue: 0/66/105
Red: 190/30/45

Target Market(s)

Business / Professionals / Chief Executives of Companies with more than 1000 employees

Industry/Entity Type

Business

Font styles to use
Serif

Colors
0255a3
ffffff

Requirements
Must have
• The title should make them pause and say "I need to get this book if I want my company to survive another 20 years!"
Nice to have
• Some image that signifies the future and / or uncertainty. Should be abstract - not people, not technology (which could change and then make the book look old). If you'd like to make the design a wrap from front to back, that is fine. I am not sure what text will go on the back at this point, so I may have to come back to you in a few months for an update.

```html
<!DOCTYPE html>
<html lang="en">
<head>
<meta charset="utf-8">
<title>Weatherizing Your Enterprise – Book Cover Wrap</title>
<link href="https://fonts.googleapis.com/css2?family=Bebas+Neue&family=Crimson+Text&family=Arimo:wght@400;700&display=swap" rel="stylesheet">
<style>
  :root {
    --stage: #b1b1b1;
    --blue-deep: #004a7c;
    --blue-mid: #0a6fae;
    --blue-bright: #1aa6dc;
    --green: #86c22a;
    --green-soft: #5cb85a;
    --teal: #1e9ba6;
    --white: #ffffff;
    --ink: #0d1b26;
    --line: rgba(160, 215, 240, 0.45);
  }
  * { margin: 0; padding: 0; box-sizing: border-box; }
  html, body { width: 1200px; height: 975px; overflow: hidden; background: var(--stage); }
  .wrap {
    position: absolute; left: 189px; top: 175px;
    width: 821px; height: 623px; display: flex;
  }
  .panel { position: relative; overflow: hidden; height: 100%; }
  .back {
    width: 389px;
    background: linear-gradient(165deg, var(--blue-bright) 0%, var(--blue-mid) 45%, var(--blue-deep) 100%);
  }
  .front {
    width: 389px;
    background: linear-gradient(200deg, var(--blue-deep) 0%, var(--blue-mid) 40%, var(--blue-bright) 100%);
  }
  .spine {
    width: 43px; background: var(--green);
    display: flex; align-items: center; justify-content: center;
  }
  .spine-title {
    writing-mode: vertical-rl; transform: rotate(180deg);
    font-family: "Arimo", sans-serif; font-size: 17px; color: var(--white);
    letter-spacing: 0.3px; white-space: nowrap;
  }
  .orb {
    position: absolute; border-radius: 50%;
    background: linear-gradient(160deg, var(--teal) 0%, var(--green-soft) 100%);
  }
  .texture { position: absolute; inset: 0; }
  .dash { position: absolute; height: 3px; border-radius: 2px; background: var(--line); }
  .callout {
    position: absolute; left: 55px; top: 123px; width: 278px; height: 300px;
    border-radius: 8px; background: rgba(180, 225, 245, 0.28);
    display: flex; align-items: center; justify-content: center; text-align: center;
    font-family: "Crimson Text", serif; font-size: 35px; line-height: 49px; color: var(--ink);
  }
  .brand-tab {
    position: absolute; left: 0; top: 0; width: 131px; height: 65px;
    background: var(--white); border-bottom-right-radius: 26px;
    display: flex; flex-direction: column; align-items: center; justify-content: center;
  }
  .brand-name {
    font-family: "Arimo", sans-serif; font-weight: 700; font-size: 15px;
    color: var(--blue-deep); line-height: 1.1; text-align: center;
  }
  .brand-tagline {
    font-family: "Arimo", sans-serif; font-weight: 700; font-size: 5px;
    color: var(--blue-deep); margin-top: 3px;
  }
  .title {
    position: absolute; left: 0; right: 0; top: 232px; text-align: center;
    font-family: "Bebas Neue", sans-serif; color: var(--white);
    font-size: 52px; line-height: 48px; letter-spacing: 0.5px;
  }
  .subtitle {
    position: absolute; left: 0; right: 0; top: 331px;
    display: flex; align-items: center; justify-content: center; gap: 10px;
    font-family: "Crimson Text", serif; font-size: 13px; color: var(--white);
  }
  .subtitle svg { display: block; }
  .author {
    position: absolute; right: 28px; top: 584px;
    font-family: "Arimo", sans-serif; font-size: 14px; color: var(--white);
  }
</style>
</head>
<body>
  <div class="wrap">
    <section class="panel back">
      <div class="texture" role="img" aria-label="Soft clouds and a faint network of linked hexagons across the blue sky"></div>
      <div class="orb" style="left:227px; top:1px; width:192px; height:192px;"></div>
      <div class="orb" style="left:-33px; top:409px; width:96px; height:96px;"></div>
      <div class="dash" style="left:0; top:397px; width:28px;"></div>
      <div class="dash" style="left:36px; top:420px; width:60px;"></div>
      <div class="dash" style="left:214px; top:452px; width:50px;"></div>
      <div class="dash" style="left:214px; top:459px; width:92px;"></div>
      <div class="dash" style="left:198px; top:550px; width:40px;"></div>
      <div class="callout">A survival<br>guide for<br>21st century<br>business</div>
    </section>

    <section class="panel spine">
      <span class="spine-title">WEATHERIZING YOUR ENTERPRISE</span>
    </section>

    <section class="panel front">
      <div class="texture" role="img" aria-label="Soft clouds and a faint network of linked hexagons across the blue sky"></div>
      <div class="orb" style="left:-43px; top:107px; width:108px; height:108px;"></div>
      <div class="orb" style="left:227px; top:441px; width:208px; height:208px;"></div>
      <div class="dash" style="left:197px; top:72px; width:50px;"></div>
      <div class="dash" style="left:214px; top:164px; width:94px;"></div>
      <div class="dash" style="left:214px; top:171px; width:48px;"></div>
      <div class="dash" style="left:0; top:201px; width:74px;"></div>
      <div class="dash" style="left:0; top:215px; width:56px;"></div>
      <div class="dash" style="left:214px; top:375px; width:64px;"></div>

      <div class="brand-tab">
        <span class="brand-name">The Lesson<br>Medic</span>
        <span class="brand-tagline">better learning at work</span>
      </div>

      <h1 class="title">WEATHERIZING<br>YOUR ENTERPRISE</h1>
      <p class="subtitle">
        <svg width="26" height="6" viewBox="0 0 26 6"><line x1="0" y1="3" x2="20" y2="3" stroke="#fff" stroke-width="1"/><circle cx="22.5" cy="3" r="2.2" fill="none" stroke="#fff" stroke-width="1"/></svg>
        by teaching thinking skills
        <svg width="26" height="6" viewBox="0 0 26 6"><circle cx="3.5" cy="3" r="2.2" fill="none" stroke="#fff" stroke-width="1"/><line x1="6" y1="3" x2="26" y2="3" stroke="#fff" stroke-width="1"/></svg>
      </p>
      <p class="author">Dr. Lorinda Haskell</p>
    </section>
  </div>
</body>
</html>
```